Feminine Health and Beauty Manufacture Needs simple clean box design

We need a box design to brand our multi line of products for women in the health and beauty market. The box will be 4" wide by 8" long and 3" deep.The design should incorporate colorful geometric or art deco patterns . I have attached a starting point for general direction on our first line called "Bloom" Luxury Bloom Mask . My sketch shows a chalk board black surrounded by the colorful pattern with the word Bloom in white script. looking for your creative input, design doesn't have to follow sketch, just and idea Good luck!
Reason: Out of town
Target Market(s)
25-60 year old women
Industry/Entity Type
Health
Look and feel

```html
<!DOCTYPE html>
<html lang="en">
<head>
<meta charset="utf-8">
<title>Bloom – Luxury Bloom Mask box dieline</title>
<link rel="stylesheet" href="https://fonts.googleapis.com/css2?family=Great+Vibes&family=Roboto+Slab:wght@400&display=swap">
<style>
  :root {
    --panel-light: #8bcfe0;
    --panel-edge: #2aa3c6;
    --band-teal: #27a2c4;
    --label-teal: #36a9c9;
    --gold: #d9b65a;
    --gold-light: #f3e3a6;
    --chalk: #3b3b3b;
    --chalk-dark: #2f2f2f;
    --white: #ffffff;
  }
  html, body {
    margin: 0;
    padding: 0;
    overflow: hidden;
    background: #ffffff;
  }
  .dieline {
    position: relative;
    width: 1200px;
    height: 749px;
    overflow: hidden;
    background: #ffffff;
  }
  .panel {
    position: absolute;
    box-sizing: border-box;
    background: var(--panel-light);
    border: 3px solid var(--panel-edge);
  }
  .flap-top { left: 165px; top: 0; width: 870px; height: 160px; }
  .flap-bottom { left: 165px; top: 589px; width: 870px; height: 160px; }
  .side-left-upper { left: 0; top: 155px; width: 168px; height: 148px; }
  .side-left-lower { left: 0; top: 455px; width: 168px; height: 136px; }
  .side-right-upper { left: 1032px; top: 155px; width: 168px; height: 148px; }
  .side-right-lower { left: 1032px; top: 455px; width: 168px; height: 136px; }

  .face-pattern {
    position: absolute;
    left: 168px; top: 158px;
    width: 864px; height: 431px;
    background:
      radial-gradient(ellipse at 30% 30%, rgba(243, 227, 166, 0.35), transparent 60%),
      radial-gradient(ellipse at 75% 75%, rgba(217, 182, 90, 0.3), transparent 60%),
      #8fd0df;
  }

  .wrap-band {
    position: absolute;
    left: 4px; top: 305px;
    width: 1192px; height: 148px;
    box-sizing: border-box;
    background: var(--band-teal);
    border: 4px solid var(--gold);
    box-shadow: inset 0 0 0 1px var(--gold-light);
  }

  .brand-label {
    position: absolute;
    box-sizing: border-box;
    border: 2px solid var(--gold);
    padding: 5px;
    background: var(--panel-light);
  }
  .brand-label .label-inner {
    width: 100%; height: 100%;
    background: var(--label-teal);
    display: flex; align-items: center; justify-content: center;
  }
  .label-top { left: 404px; top: 37px; width: 381px; height: 85px; transform: rotate(180deg); }
  .label-bottom { left: 415px; top: 628px; width: 381px; height: 85px; }

  .brand-name {
    font-family: "Roboto Slab", Georgia, serif;
    font-weight: 400;
    color: var(--white);
    letter-spacing: 0.5px;
    white-space: nowrap;
    line-height: 1;
  }
  .label-inner .brand-name { font-size: 40px; }

  .chalkboard {
    position: absolute;
    left: 316px; top: 258px;
    width: 574px; height: 240px;
    background: radial-gradient(ellipse at center, var(--chalk) 0%, var(--chalk-dark) 100%);
  }
  .chalkboard-frame {
    position: absolute;
    inset: 10px 10px 12px 10px;
    border: 2px solid var(--white);
  }
  .product-name {
    position: absolute;
    left: 32px; top: 26px;
    margin: 0;
    font-family: "Great Vibes", cursive;
    font-weight: 400;
    font-size: 108px;
    line-height: 1;
    color: var(--white);
  }
  .product-line {
    position: absolute;
    left: 248px; top: 140px;
    margin: 0;
    font-family: "Great Vibes", cursive;
    font-size: 34px;
    line-height: 1;
    color: var(--white);
    transform: rotate(-9deg);
    transform-origin: left center;
    white-space: nowrap;
  }
  .swash {
    position: absolute;
    left: 0; top: 0;
    width: 574px; height: 240px;
  }
  .chalkboard .brand-name {
    position: absolute;
    left: 344px; top: 54px;
    font-size: 24px;
  }
</style>
</head>
<body>
<main class="dieline">
  <div class="panel flap-top"></div>
  <div class="panel flap-bottom"></div>
  <div class="panel side-left-upper"></div>
  <div class="panel side-left-lower"></div>
  <div class="panel side-right-upper"></div>
  <div class="panel side-right-lower"></div>

  <div class="face-pattern" role="img" aria-label="Gold line-art leaf pattern on light aqua background"></div>

  <div class="wrap-band"></div>

  <div class="brand-label label-top">
    <div class="label-inner"><span class="brand-name">petal&amp;dew</span></div>
  </div>
  <div class="brand-label label-bottom">
    <div class="label-inner"><span class="brand-name">petal&amp;dew</span></div>
  </div>

  <section class="chalkboard">
    <div class="chalkboard-frame"></div>
    <svg class="swash" viewBox="0 0 574 240" aria-hidden="true">
      <path d="M114 214 C 250 190, 400 150, 548 140" fill="none" stroke="#ffffff" stroke-width="3" stroke-linecap="round"/>
    </svg>
    <h1 class="product-name">Bloom</h1>
    <p class="product-line">Luxury Bloom Mask</p>
    <span class="brand-name">petal&amp;dew</span>
  </section>
</main>
</body>
</html>
```